Kestrel Homes Australia Business Card

We need a Business Card design for our new start up company.
A unique model designed to address Australia’s growing housing affordability problem has been launched. More than half of Australians are being priced out of the property market and have resigned themselves to the fact that they may never be able to afford a home.
We have developed a unique Algorithm that allows people to get into property and reverse this trend of domination by the property investors in this country. The first of its kind model facilitates connecting people to lending facilities that do not require them to have the finance combined under the purchase contract.
Ownership is shared with a second-tier investor, made up of either family or friends if not, Kestrel Homes Australia will provide a mini property investor enabling thousands of people the opportunity to buy a home, which they otherwise thought was not possible.
Kestrel Homes Australia is addressing housing affordability for families and individuals, giving every Australian looking to buy a home the opportunity to enter the property market to live in or invest.
Under our unique model, there is no combined finance, and individuals are assessed for their percentage portion of the property only. “A unique feature of our product is it is based around the strategies used for property investment. I have developed a unique Algorithm that enables the Home buyer to purchase 60% of a property, while Kestrel Homes Australia facilitates a second-tier investor to buy the other 40%. The Algorithm locks the investor in place and enables the home buyer to stairway to full ownership. The investment is secured against real property.
Please refer to our website www.kestrelhomes.com.au for inspiration.
Also please find attached our logo.
Any further directions please ask.
Cheers Marcus
Industry/Entity Type
Real Estate
Contact Information for Business Card
Marcus Thorley
CEO
Mobile 0400 615 272
www.kestrelhomes.com.au
Email: marcus@kestrelhomes.com.au
Colors
Designer to choose colors to be used in the design.
Look and feel

```html
<!DOCTYPE html>
<html lang="en">
<head>
<meta charset="utf-8">
<title>Kestrel Homes Australia – Business Card</title>
<link rel="stylesheet" href="https://fonts.googleapis.com/css2?family=Open+Sans:wght@400;600;700&display=swap">
<style>
  :root {
    --stage: #e9e7e4;
    --card: #1b1c1e;
    --teal: #2aa3c9;
    --green: #4f9a2c;
    --white: #f2f2f2;
    --grey: #9a9a9a;
    --rule: #bfbfbf;
  }
  * { box-sizing: border-box; margin: 0; padding: 0; }
  html, body {
    width: 1200px; height: 864px; overflow: hidden;
    background: var(--stage);
    font-family: "Open Sans", Arial, sans-serif;
  }
  .sheet {
    width: 1200px; height: 864px;
    display: flex; flex-direction: column;
    align-items: center; justify-content: center; gap: 40px;
  }
  .card {
    width: 660px; height: 377px;
    background: var(--card);
    position: relative;
    box-shadow: 0 6px 18px rgba(0,0,0,.25);
  }
  .brand {
    display: flex; flex-direction: column; align-items: flex-start;
  }
  .brand__mark {
    display: flex; align-items: center; gap: 10px;
  }
  .brand__dot {
    width: 14px; height: 14px; border-radius: 50%; background: var(--teal);
  }
  .brand__name {
    color: var(--teal); font-weight: 700; font-size: 30px; letter-spacing: .2px; white-space: nowrap;
  }
  .brand__tagline {
    color: var(--green); font-weight: 600; font-size: 17px; margin-top: 2px; margin-left: 24px; white-space: nowrap;
  }

  /* logo side */
  .card--logo .brand { position: absolute; left: 92px; top: 118px; }
  .card--logo .site {
    position: absolute; left: 116px; top: 234px;
    color: var(--grey); font-size: 15px; letter-spacing: 5px; white-space: nowrap;
  }

  /* contact side */
  .card--contact .brand { position: absolute; left: 120px; top: 82px; }
  .person {
    position: absolute; left: 80px; top: 196px; width: 200px; text-align: right;
  }
  .person__name { color: var(--teal); font-weight: 700; font-size: 17px; text-transform: uppercase; white-space: nowrap; }
  .person__title { color: var(--green); font-weight: 600; font-size: 17px; margin-top: 2px; }
  .divider {
    position: absolute; left: 300px; top: 192px; width: 1.5px; height: 92px; background: var(--rule);
  }
  .contacts {
    position: absolute; left: 322px; top: 196px; list-style: none;
  }
  .contacts li {
    display: flex; align-items: center; gap: 10px;
    color: var(--white); font-size: 16px; line-height: 26px; white-space: nowrap;
  }
  .contacts svg { width: 13px; height: 13px; fill: var(--teal); flex: none; }
</style>
</head>
<body>
<main class="sheet">

  <section class="card card--logo">
    <div class="brand">
      <div class="brand__mark"><span class="brand__dot"></span><span class="brand__name">Kestrel Homes Australia</span></div>
      <div class="brand__tagline">Opening Doors to Owning a Home</div>
    </div>
    <div class="site">www.kestrelhomes.com.au</div>
  </section>

  <section class="card card--contact">
    <div class="brand">
      <div class="brand__mark"><span class="brand__dot"></span><span class="brand__name">Kestrel Homes Australia</span></div>
      <div class="brand__tagline">Opening Doors to Owning a Home</div>
    </div>
    <div class="person">
      <div class="person__name">Marcus Thorley</div>
      <div class="person__title">CEO</div>
    </div>
    <div class="divider"></div>
    <ul class="contacts">
      <li>
        <svg viewBox="0 0 12 12" aria-hidden="true"><path d="M3 0h6a1 1 0 0 1 1 1v10a1 1 0 0 1-1 1H3a1 1 0 0 1-1-1V1a1 1 0 0 1 1-1zm0 1.5v8h6v-8z"/></svg>
        0400615272
      </li>
      <li>
        <svg viewBox="0 0 12 12" aria-hidden="true"><path d="M0 2h12v1L6 7 0 3z M0 4.5l6 4 6-4V10H0z"/></svg>
        marcus@kestrelhomes.com.au
      </li>
      <li>
        <svg viewBox="0 0 12 12" aria-hidden="true"><circle cx="6" cy="6" r="6"/><circle cx="6" cy="6" r="2.5" fill="#1b1c1e"/></svg>
        www.kestrelhomes.com.au
      </li>
    </ul>
  </section>

</main>
</body>
</html>
```